Coaching business needs flyer for business market

I need a flyer that I can send to HR-managers and business owners to inform them of my coaching services for organisations. We have three services: organisational- and teamcoaching, individual coaching and training programs.
I want the flyer to express calmness, solid and trustworthy coaching. As a person I am open and think out of the box.

In my logo I use a couple of colours (blue, green, orange and grey) that represent the diversity of humans. My company's name is Bramblecrest Engagement & Coaching and tag line is "Awaken your quiet river".

I do not want the design to be too busy but also not too boring. I tried making something myself. Feel free to build on that design. Or feel free to start from scratch.

```html
<!DOCTYPE html>
<html lang="nl">
<head>
<meta charset="utf-8">
<title>Bramblecrest Engagement &amp; Coaching</title>
<link href="https://fonts.googleapis.com/css2?family=Open+Sans:wght@400;700&family=Caveat:wght@400&display=swap" rel="stylesheet">
<style>
  :root {
    --ink: #1f1f1f;
    --grey: #5a5c60;
    --grey-light: #d8d8d8;
    --footer: #55575a;
    --blue: #3b55b5;
    --red: #de5138;
    --teal: #3ccfcf;
    --orange: #f5a030;
    --tan: #c79a6e;
    --white: #ffffff;
  }
  * { margin: 0; padding: 0; box-sizing: border-box; }
  html, body { width: 848px; height: 1200px; overflow: hidden; background: var(--white); }
  body { font-family: "Open Sans", sans-serif; color: var(--ink); position: relative; }

  .corner-texture {
    position: absolute; right: 0; top: 0; width: 160px; height: 145px;
    background: radial-gradient(circle at 100% 20%, #c9c9c9 0%, #e4e4e4 35%, rgba(255,255,255,0) 75%);
  }

  .brand { position: absolute; text-align: center; color: var(--grey); font-weight: 400; }
  .brand-mark { display: block; margin: 0 auto 4px; width: 48px; height: 48px; border: 2px solid #9a9ca0; border-radius: 50%; }
  .brand-name { display: block; font-size: 27px; line-height: 30px; letter-spacing: 0.5px; }
  .brand-sub { display: block; font-size: 12.5px; line-height: 16px; letter-spacing: 0.3px; }
  .brand-top { left: 74px; top: 25px; width: 162px; }
  .brand-bottom { left: 638px; top: 990px; width: 162px; }

  .tagline {
    position: absolute; left: 255px; top: 70px;
    font-family: "Caveat", cursive; font-size: 40px; color: var(--orange); line-height: 48px;
  }

  .photo {
    position: absolute; left: -6px; width: 227px; height: 174px;
    border: 4px solid; border-radius: 0 27px 27px 0;
  }
  .photo-portrait { top: 159px; border-color: var(--tan); background: linear-gradient(135deg, #3e56c8, #5a6fd0 55%, #a07a62); }
  .photo-team { top: 361px; border-color: var(--red); background: linear-gradient(135deg, #c9b8a6, #8c7d70 50%, #e2d6c8); }
  .photo-individual { top: 563px; border-color: var(--teal); background: linear-gradient(135deg, #d8d2c6, #b7b0a4 55%, #3c3f48); }
  .photo-training { top: 766px; border-color: var(--orange); background: linear-gradient(135deg, #2a2630, #4a3f52 50%, #1e1c22); }

  .divider { position: absolute; left: 0; width: 848px; height: 1px; background: var(--grey-light); }

  .intro {
    position: absolute; left: 254px; top: 165px; width: 570px;
    font-size: 14px; line-height: 19.2px;
  }
  .intro strong { color: var(--blue); font-weight: 700; }

  .service-title {
    position: absolute; left: 254px; width: 580px;
    font-size: 15.6px; line-height: 21.5px; font-weight: 700;
  }
  .title-team { top: 379px; color: var(--red); }
  .title-individual { top: 582px; color: var(--teal); }
  .title-training { top: 785px; color: var(--orange); }

  .list { position: absolute; list-style: none; font-size: 14px; line-height: 19.3px; }
  .list li { position: relative; padding-left: 24px; }
  .list li::before {
    content: ""; position: absolute; left: 7px; top: 8px;
    width: 5px; height: 5px; border-radius: 50%; background: var(--ink);
  }
  .list-team { left: 254px; top: 440px; }
  .list-individual { left: 254px; top: 621px; }
  .list-training { left: 254px; top: 845px; }
  .list-methods { left: 32px; top: 1011px; width: 520px; }

  .methods-title {
    position: absolute; left: 32px; top: 969px;
    font-size: 15.5px; font-weight: 700; color: var(--ink);
  }

  .footer {
    position: absolute; left: 0; top: 1140px; width: 848px; height: 60px;
    background: var(--footer); color: var(--white);
  }
  .contact {
    position: absolute; top: 18px; display: flex; align-items: center; gap: 10px;
    font-size: 17px; line-height: 24px;
  }
  .contact svg { width: 22px; height: 22px; flex: none; }
  .contact-phone { left: 67px; }
  .contact-mail { left: 330px; }
  .contact-web { left: 585px; }
</style>
</head>
<body>

<div class="corner-texture" role="img" aria-label="Zachte grijze stippen als decoratie"></div>

<div class="brand brand-top">
  <span class="brand-mark"></span>
  <span class="brand-name">bramblecrest</span>
  <span class="brand-sub">engagement &amp; coaching</span>
</div>

<div class="tagline">Awaken your quiet river</div>

<div class="photo photo-portrait" role="img" aria-label="Portretfoto van de trainer en coach"></div>
<p class="intro"><strong>MARIELLE DOORNBOS</strong> is trainer en coach. Ze heeft ruime ervaring met veranderingstrajecten binnen organisaties. Mensen omschrijven haar als ‘betrokken, warm, stevig en kordaat’. Het is haar passie om organisaties, teams en mensen te helpen groeien. Zij helpt weerstand te overwinnen en draagt bij aan groei in zelfvertrouwen. Haar trainingen en coaching zijn erop gericht om snel inzichtelijk te krijgen welke stappen men moet zetten om verder te komen. Ze gelooft de veranderkracht van de mensen waar ze mee werkt. Ze is er om steun en richting te bieden en laat hen zelf aan het roer.</p>

<div class="divider" style="top:347px"></div>

<div class="photo photo-team" role="img" aria-label="Foto van een teamcoachingsessie met deelnemers in een kring"></div>
<h2 class="service-title title-team">Een organisatie waar medewerkers gemotiveerd zijn, samenwerken, communiceren zonder gedoe door ORGANISATIE- of TEAM coaching:</h2>
<ul class="list list-team">
  <li>Heb je zorgen voor of na een fusie of verandering?</li>
  <li>Wil je missie, visie &amp; strategie ontwikkelen of wijzigen?</li>
  <li>Wens je de cultuur-veranderen of verder ontwikkelen?</li>
  <li>Beoog je de samenwerking bevorderen of verbeteren?</li>
</ul>

<div class="divider" style="top:550px"></div>

<div class="photo photo-individual" role="img" aria-label="Foto van de coach die spreekt in een lichte ruimte met bloemen"></div>
<h2 class="service-title title-individual">Duurzame Inzetbaarheid door INDIVIDUELE Coaching:</h2>
<ul class="list list-individual">
  <li>Wens je medewerkers die hun talent ten volste benutten?</li>
  <li>Verlang je meer authentieke leiderschap bij je collega’s?</li>
  <li>Wil je de mensen vooruit helpen in hun loopbaan?</li>
  <li>Zoek je steun voor medewerkers met burn-out of re-integratie?</li>
  <li>Heb je hulp nodig bij outplacement trajecten?</li>
</ul>

<div class="divider" style="top:752px"></div>

<div class="photo photo-training" role="img" aria-label="Foto van een workshop met publiek in een donkere zaal"></div>
<h2 class="service-title title-training">Ontwikkeling &amp; Borging van kennis en vakmanschap door LEERGANGEN, TRAININGEN &amp; WORKSHOPS op MAAT:</h2>
<ul class="list list-training">
  <li>Leiderschap</li>
  <li>Communicatie</li>
  <li>Leren kijken met ‘systemische blik’ voor professionals</li>
  <li>Conflicthantering</li>
</ul>

<div class="divider" style="top:955px"></div>

<h2 class="methods-title">Gedegen resultaat en kwaliteit door bewezen ‘best practices’</h2>
<ul class="list list-methods">
  <li>Neuro Linguïstisch Programmeren (NLP)</li>
  <li>Transactionele Analyse</li>
  <li>Systemisch Werken: Organisatieopstellingen, Familieopstellingen, Identity oriented Psycho Traumaopstellingen)</li>
  <li>Somatic Experience, Ademwerk en Lichaamswerk</li>
</ul>

<div class="brand brand-bottom">
  <span class="brand-mark"></span>
  <span class="brand-name">bramblecrest</span>
  <span class="brand-sub">engagement &amp; coaching</span>
</div>

<footer class="footer">
  <div class="contact contact-phone">
    <svg viewBox="0 0 22 22"><circle cx="11" cy="11" r="11" fill="#fff"/><rect x="7.5" y="5" width="7" height="12" rx="1.5" fill="none" stroke="#55575a" stroke-width="1.5"/><line x1="10" y1="15" x2="12" y2="15" stroke="#55575a" stroke-width="1.2"/></svg>
    <span>+31-6-12 34 56 78</span>
  </div>
  <div class="contact contact-mail">
    <svg viewBox="0 0 22 22"><circle cx="11" cy="11" r="11" fill="#fff"/><rect x="5" y="7" width="12" height="8.5" rx="1" fill="none" stroke="#55575a" stroke-width="1.4"/><polyline points="5.5,7.5 11,12 16.5,7.5" fill="none" stroke="#55575a" stroke-width="1.4"/></svg>
    <span>info@bramblecrest.nu</span>
  </div>
  <div class="contact contact-web">
    <svg viewBox="0 0 22 22"><circle cx="11" cy="11" r="11" fill="#fff"/><circle cx="11" cy="11" r="6" fill="none" stroke="#55575a" stroke-width="1.3"/><ellipse cx="11" cy="11" rx="2.6" ry="6" fill="none" stroke="#55575a" stroke-width="1.2"/><line x1="5" y1="11" x2="17" y2="11" stroke="#55575a" stroke-width="1.2"/></svg>
    <span>www.bramblecrest.nu</span>
  </div>
</footer>

</body>
</html>
```